Beard Balm Label

Hi Chaps,

We are needing a label for a new product we are adding to our international beard grooming range.

The design needs to be on a circular label. There will be a top label (that will contain the branding and what the product is) and a bottom label (that will contain the instructions for use and ingredients).

The size of the top label is 75mm in diameter.

The size of the bottom label is 68mm in diameter

It needs to align with our branding from our Beard Oil and Moustache wax product. checkout www.thegrizzledgent.com to get an insight of this.

What needs to be on the label:

- The grizzled gent logo (logo attached)
- Hearthside Beard Balm
- the words "Quality Craftsmanship" "Handmade in Australia" "Protect, Condition, Style"
- "Our all natural Hearthside Beard Balm is made in ABSURDLY small batches and will help you keep even the wildest beard looking sharp, lush and smelling great."
-TheGrizzledGent.com

*all fonts are attached

Information on the bottom label is not important at this stage and will provide the detail after a winner has been chosen.

This project will be open for 5 days.

Any questions, please ask asap.

```html
<!DOCTYPE html>
<html lang="en">
<head>
<meta charset="utf-8">
<title>Hearthside Beard Balm – Label</title>
<link rel="stylesheet" href="https://fonts.googleapis.com/css2?family=Alfa+Slab+One&family=Roboto+Slab:wght@700;800&display=swap">
<style>
  :root {
    --backdrop: #6d8181;
    --label: #ffffff;
    --ink: #111111;
    --rule: #777777;
  }
  * { margin: 0; padding: 0; box-sizing: border-box; }
  html, body { width: 1200px; height: 1000px; overflow: hidden; background: var(--backdrop); }
  .canvas { position: relative; width: 1200px; height: 1000px; background: var(--backdrop); color: var(--ink); }

  .label { position: absolute; border-radius: 50%; background: var(--label); }
  .label--top { left: 56px; top: 50px; width: 624px; height: 624px; }
  .label--bottom { left: 620px; top: 434px; width: 540px; height: 540px; }

  .arc-text { position: absolute; left: 0; top: 0; width: 1200px; height: 1000px; pointer-events: none; }
  .arc-text text { font-family: "Alfa Slab One", serif; font-size: 25px; fill: var(--ink); letter-spacing: 1px; }

  .abs { position: absolute; text-align: center; white-space: nowrap; }

  .brand-name {
    left: 200px; width: 336px; top: 160px;
    font-family: "Alfa Slab One", serif; font-size: 44px; line-height: 1.1;
    text-transform: uppercase; color: var(--ink);
  }

  .product-kicker {
    left: 168px; width: 400px; top: 378px;
    font-family: "Alfa Slab One", serif; font-size: 33px; line-height: 1;
  }
  .product-name {
    left: 130px; width: 476px; top: 420px;
    font-family: "Alfa Slab One", serif; font-size: 44px; line-height: 1; letter-spacing: 1px;
  }
  .benefits {
    left: 168px; width: 400px; top: 494px;
    font-family: "Roboto Slab", serif; font-weight: 800; font-size: 35px; line-height: 44px;
  }

  .rule { position: absolute; height: 0; border-top: 1px dotted var(--rule); }
  .rule--double { height: 3px; border-top: 1px solid var(--rule); border-bottom: 1px solid var(--rule); }

  .blurb {
    left: 700px; width: 380px; top: 540px;
    font-family: "Roboto Slab", serif; font-weight: 800; font-size: 17px; line-height: 23px;
    text-transform: uppercase;
  }
  .blurb-emphasis {
    display: flex; align-items: center; justify-content: center; gap: 8px;
    font-family: "Alfa Slab One", serif; font-weight: 400; font-size: 32px; line-height: 46px;
  }
  .hatch { width: 40px; height: 10px;
    background: repeating-linear-gradient(90deg, var(--rule) 0 1px, transparent 1px 4px); }

  .site-address {
    left: 700px; width: 380px; top: 888px;
    font-family: "Roboto Slab", serif; font-weight: 800; font-size: 22px; letter-spacing: 0.5px;
  }
</style>
</head>
<body>
<main class="canvas">
  <section class="label label--top" aria-label="Top label"></section>
  <section class="label label--bottom" aria-label="Bottom label"></section>

  <div class="abs brand-name">The Grizzled<br>Gent</div>

  <div class="rule" style="left:228px; top:398px; width:36px;"></div>
  <div class="rule" style="left:472px; top:398px; width:38px;"></div>
  <div class="abs product-kicker">HEARTHSIDE</div>
  <div class="abs product-name">BEARD BALM</div>
  <div class="rule rule--double" style="left:188px; top:483px; width:362px;"></div>
  <div class="abs benefits">PROTECT<br>CONDITION<br>STYLE</div>

  <svg class="arc-text" viewBox="0 0 1200 1000" aria-hidden="false">
    <defs>
      <path id="arc-left" d="M 73 388 A 296 296 0 0 0 347 657"/>
      <path id="arc-right" d="M 399 656 A 296 296 0 0 0 663 388"/>
    </defs>
    <text><textPath href="#arc-left" startOffset="50%" text-anchor="middle">QUALITY CRAFTSMANSHIP</textPath></text>
    <text><textPath href="#arc-right" startOffset="50%" text-anchor="middle">HANDMADE IN AUSTRALIA</textPath></text>
  </svg>

  <div class="rule" style="left:723px; top:525px; width:335px;"></div>
  <div class="abs blurb">
    Our all natural Hearthside<br>beard balm is made in
    <div class="blurb-emphasis"><span class="hatch"></span>ABSURDLY<span class="hatch"></span></div>
    Small batches and will<br>help you keep even the<br>wildest beard looking<br>sharp, lush and smelling<br>great.
  </div>
  <div class="rule" style="left:828px; top:767px; width:125px;"></div>

  <div class="abs site-address">TheGrizzledGent.com</div>
</main>
</body>
</html>
```